この度はまことにありがとうございます。
広告代理店です。

のぼりデザインのアイデアを頂戴できればと思っております。

入れる文字は下記になります。
梅 の さ と ・ ひ な た べ

ご不明な点などございましたらお気兼ねなくご連絡ください。
何卒、宜しくお願い申し上げます。
サイズの記載がございませんでした。

1800mm縦
600mmよこ

ロゴを縦組みいただいてもかまいません。

何卒、よろしくお願いします。
皆様のご提案に心より感謝申し上げます。

追記
目的をあらためてお知らせします。

このロゴだと背景色が白になりがちです。
しかしながらのぼりを外で使用する場合、背景に色を使わないと目立たないように感じます。

ロゴのイメージを崩さず少し目立つ(目立ちすぎなくて結構です。)のぼりが作れるかを
ご提案いただきたいのが今回の趣旨でございます。

もう1点は洋食っぽい?欧米風?の雰囲気といいますかおしゃれな感じを希望しています。
おしゃれさはかなりのポイントです。

結果的に背景白になるかもですが、、、。
背景が白がNGというわけではなくポイントでどう色を使うかです。

何卒、宜しくお願い申し上げます。

イメージに合うとても素敵なデザインでした。

この度はまことにありがとうございます。
皆様のご提案に心より感謝申し上げます。
また機会がございましたらよろしくお願い申し上げます。

```html
<!DOCTYPE html>
<html lang="ja">
<head>
<meta charset="utf-8">
<title>のぼりデザイン案 梅のさと・ひなたべ</title>
<link href="https://fonts.googleapis.com/css2?family=Noto+Sans+JP:wght@400;700&family=Zen+Maru+Gothic:wght@500;700&display=swap" rel="stylesheet">
<style>
  :root {
    --paper: #ffffff;
    --ink: #1a1a1a;
    --rule: #9a9a9a;
    --brown-light: #b8855a;
    --brown-mid: #8a5a33;
    --brown-deep: #5e3a1e;
    --accent-light: #f29a5c;
    --accent-mid: #e86b3c;
    --accent-deep: #d2452a;
    --tree-tone: rgba(226, 212, 196, 0.85);
    --tree-tone-2: rgba(238, 229, 218, 0.55);
    --illust-tone: rgba(217, 180, 138, 0.9);
    --illust-tone-2: rgba(217, 180, 138, 0.35);
    --roman-green: #6f9a3c;
  }
  * { margin: 0; padding: 0; box-sizing: border-box; }
  html, body { width: 849px; height: 1200px; overflow: hidden; background: var(--paper); }
  body { position: relative; font-family: "Noto Sans JP", sans-serif; color: var(--ink); }

  .sheet-title { position: absolute; left: 12px; top: 10px; font-size: 17px; font-weight: 700; }

  .variation { position: absolute; top: 86px; width: 340px; }
  .variation--one { left: 52px; }
  .variation--two { left: 444px; }
  .variation-label { font-size: 11px; margin-left: 6px; margin-bottom: 10px; }

  .tab-holder { position: relative; }
  .banner {
    position: relative; margin-left: 10px; width: 326px; height: 977px;
    border: 1px solid var(--rule); background: var(--paper); overflow: hidden;
  }
  .sleeve-tab {
    position: absolute; left: -10px; width: 18px; height: 10px;
    border: 1px solid var(--rule); background: var(--paper); z-index: 1;
  }
  .sleeve-tab:nth-of-type(1) { top: 124px; }
  .sleeve-tab:nth-of-type(2) { top: 350px; }
  .sleeve-tab:nth-of-type(3) { top: 576px; }
  .sleeve-tab:nth-of-type(4) { top: 802px; }

  .crest-illustration {
    position: absolute; left: 40px; top: 18px; width: 246px; height: 136px;
    background: radial-gradient(closest-side, var(--illust-tone) 0%, var(--illust-tone-2) 55%, rgba(255,255,255,0) 100%);
  }
  .tree-illustration {
    position: absolute; left: -20px; bottom: -40px; width: 366px; height: 620px;
    background: radial-gradient(closest-side, var(--tree-tone) 0%, var(--tree-tone-2) 60%, rgba(255,255,255,0) 100%);
  }

  .name-column {
    position: absolute; left: 0; right: 0; top: 178px;
    display: flex; flex-direction: column; align-items: center; gap: 4px;
  }
  .name-disc {
    width: 74px; height: 74px; border-radius: 50%;
    display: flex; align-items: center; justify-content: center;
    font-family: "Zen Maru Gothic", sans-serif; font-weight: 700; font-size: 42px; line-height: 1; color: var(--paper);
    background: radial-gradient(circle at 40% 38%, var(--brown-light) 0%, var(--brown-mid) 55%, var(--brown-deep) 100%);
  }
  .name-disc--accent {
    background: radial-gradient(circle at 40% 38%, var(--accent-light) 0%, var(--accent-mid) 55%, var(--accent-deep) 100%);
  }
  .name-dot { width: 8px; height: 8px; border-radius: 50%; background: var(--brown-mid); margin: 4px 0; }

  .roman-name {
    position: absolute; left: 0; right: 0; bottom: 40px; text-align: center;
    font-family: "Zen Maru Gothic", sans-serif; font-size: 13px; letter-spacing: 1.5px; color: var(--roman-green);
  }

  .title-block {
    position: absolute; left: 12px; right: 12px; top: 1110px; height: 46px;
    display: grid; grid-template-columns: 120px 1fr 1fr 1fr; border: 1px solid var(--ink);
  }
  .title-block__mark { background: var(--ink); }
  .title-block__cell { border-left: 1px solid var(--ink); padding: 3px 5px; font-size: 8px; color: #444; }
</style>
</head>
<body>
  <h1 class="sheet-title">◆デザイン</h1>

  <section class="variation variation--one">
    <p class="variation-label">■カラーバリエーション❶</p>
    <div class="tab-holder">
      <span class="sleeve-tab"></span><span class="sleeve-tab"></span><span class="sleeve-tab"></span><span class="sleeve-tab"></span>
      <div class="banner">
        <div class="tree-illustration" role="img" aria-label="淡いベージュの木のシルエットの背景イラスト"></div>
        <div class="crest-illustration" role="img" aria-label="木の枝と水鳥の親子のイラスト"></div>
        <div class="name-column">
          <span class="name-disc">梅</span><span class="name-disc">の</span><span class="name-disc">さ</span><span class="name-disc">と</span>
          <span class="name-dot"></span>
          <span class="name-disc">ひ</span><span class="name-disc">な</span><span class="name-disc">た</span><span class="name-disc">べ</span>
        </div>
        <p class="roman-name">ume no sato hinatabe</p>
      </div>
    </div>
  </section>

  <section class="variation variation--two">
    <p class="variation-label">■カラーバリエーション❷</p>
    <div class="tab-holder">
      <span class="sleeve-tab"></span><span class="sleeve-tab"></span><span class="sleeve-tab"></span><span class="sleeve-tab"></span>
      <div class="banner">
        <div class="tree-illustration" role="img" aria-label="淡いベージュの木のシルエットの背景イラスト"></div>
        <div class="crest-illustration" role="img" aria-label="木の枝と水鳥の親子のイラスト"></div>
        <div class="name-column">
          <span class="name-disc">梅</span><span class="name-disc">の</span><span class="name-disc">さ</span><span class="name-disc">と</span>
          <span class="name-dot"></span>
          <span class="name-disc name-disc--accent">ひ</span><span class="name-disc">な</span><span class="name-disc">た</span><span class="name-disc">べ</span>
        </div>
        <p class="roman-name">ume no sato hinatabe</p>
      </div>
    </div>
  </section>

  <footer class="title-block">
    <div class="title-block__mark"></div>
    <div class="title-block__cell">Date</div>
    <div class="title-block__cell">Customer Name</div>
    <div class="title-block__cell">Designer</div>
  </footer>
</body>
</html>
```